Step Up Personal Training Sessions

Whether you have a lot to give out or a little...just Step Up. Whether you are strong or you desire to get there... just Step Up. Stay Bold Feel Free. PT's with a passionate coach.

I had imagined black and white or indigo/white. Communicate love, people and fitness.

Target Market(s)

Women, men, disabilities. People whom wish to move more, or who do not desire to go to a gym. One on one fitness or small group training.

Industry/Entity Type

Training

Contact Information for Business Card

Kim Farrow
0431 592 604
kimjoanne@wavenet.example

Font styles to use
Decorative

Colors
0d0d0d
1b1b1b

Requirements
Must have
• Step Up
• Personal Fitness Sessions
• Stay Bold Feel Free
• ( my details above )
Nice to have
• If any part of the project description ....Whether....etc
• can be fit onto card. That would be great. I had ideas of Heart, people exercising, I love boxing training, so this idea was in my head, not sure how to bring all together. Would also like to work with disabilities.
Should not have
• Cannot think of any not haves at this stage.
• Colours at the bottom of page, either green is ok, with charcoal or navy. Not both these colours together.

```html
<!DOCTYPE html>
<html lang="en">
<head>
<meta charset="utf-8">
<title>Step Up Personal Training Sessions – Business Cards</title>
<link rel="stylesheet" href="https://fonts.googleapis.com/css2?family=Ubuntu:wght@300;400;700&display=swap">
<style>
  :root {
    --page-bg: #ebecea;
    --charcoal: #434343;
    --charcoal-text: #2f2f25;
    --ink: #2b2b2b;
    --green-top: #cdd07c;
    --green-bottom: #6ea032;
    --white: #ffffff;
    --soft-grey: #dcdcdc;
    --band-grey: #77747f;
    --orange: #ef7f1f;
    --figure-dark: #8a8a8a;
    --figure-light: #f4f4f4;
  }
  * { margin: 0; padding: 0; box-sizing: border-box; }
  html, body {
    width: 951px;
    height: 1200px;
    overflow: hidden;
    background: var(--page-bg);
    font-family: "Ubuntu", sans-serif;
  }
  .canvas { position: relative; width: 951px; height: 1200px; }

  .card {
    position: absolute;
    overflow: hidden;
    border-radius: 22px;
    box-shadow: 0 4px 14px rgba(0, 0, 0, 0.28);
  }
  .card__backdrop { position: absolute; inset: 0; width: 100%; height: 100%; }
  .card > *:not(.card__backdrop) { position: absolute; }

  .brand-name {
    font-weight: 700;
    font-size: 38px;
    letter-spacing: 0.5px;
    text-align: center;
    white-space: nowrap;
  }
  .holder-name { font-weight: 700; font-size: 27px; letter-spacing: 0.3px; }
  .holder-role { font-weight: 300; font-size: 19px; }
  .contact-row {
    display: flex;
    align-items: center;
    gap: 14px;
    font-weight: 300;
    font-size: 23px;
    white-space: nowrap;
  }
  .contact-row svg { flex: none; }

  /* Card one: green and charcoal */
  .card--green { left: 102px; top: 131px; width: 738px; height: 442px; background: var(--charcoal); }
  .card--green .brand-name { left: 40px; top: 122px; width: 176px; color: var(--charcoal-text); }
  .card--green .tagline-list {
    left: 36px; top: 232px;
    color: var(--charcoal-text);
    font-weight: 700; font-size: 22px; line-height: 32px;
    list-style: none;
  }
  .card--green .tagline-divider { font-weight: 400; letter-spacing: 1px; }
  .card--green .holder-name { left: 362px; top: 50px; color: var(--white); }
  .card--green .holder-role { left: 362px; top: 86px; color: var(--soft-grey); }
  .card--green .contact-row { left: 362px; color: var(--white); }
  .card--green .contact-row--phone { top: 122px; }
  .card--green .contact-row--email { top: 158px; }
  .card--green .activity-figures {
    left: 378px; top: 215px; width: 338px; height: 208px;
    border-radius: 10px;
    background: linear-gradient(180deg, rgba(138,138,138,0.35), rgba(138,138,138,0.55));
  }

  /* Card two: white, orange and grey */
  .card--orange { left: 100px; top: 670px; width: 726px; height: 422px; background: var(--white); }
  .card--orange .brand-name { left: 44px; top: 106px; width: 180px; color: var(--orange); }
  .card--orange .holder-name { left: 313px; top: 40px; color: var(--ink); }
  .card--orange .holder-role { left: 313px; top: 76px; color: var(--ink); }
  .card--orange .contact-row { left: 312px; color: var(--ink); }
  .card--orange .contact-row--phone { top: 111px; }
  .card--orange .contact-row--email { top: 146px; }
  .card--orange .tagline-list {
    left: 40px; top: 296px;
    color: var(--white);
    font-weight: 700; font-size: 22px; line-height: 31px;
    list-style: none;
  }
  .card--orange .tagline-list li { display: flex; align-items: center; gap: 10px; }
  .card--orange .tagline-list li::before {
    content: ""; width: 8px; height: 8px; border-radius: 50%;
    background: var(--orange);
  }
  .card--orange .activity-figures {
    left: 362px; top: 208px; width: 346px; height: 206px;
    border-radius: 10px;
    background: linear-gradient(180deg, rgba(244,244,244,0.25), rgba(244,244,244,0.45));
  }
</style>
</head>
<body>
<main class="canvas">

  <section class="card card--green" aria-label="Business card, green and charcoal version">
    <svg class="card__backdrop" viewBox="0 0 738 442" preserveAspectRatio="none" aria-hidden="true">
      <defs>
        <linearGradient id="green-panel" x1="0" y1="0" x2="0" y2="1">
          <stop offset="0" stop-color="#cdd07c"/>
          <stop offset="0.45" stop-color="#a9c15a"/>
          <stop offset="1" stop-color="#6ea032"/>
        </linearGradient>
      </defs>
      <path d="M0 0 H200 C300 80 362 240 344 442 H0 Z" fill="url(#green-panel)"/>
      <path d="M200 0 C300 80 362 240 344 442" fill="none" stroke="#ffffff" stroke-width="4"/>
    </svg>

    <div class="brand-name">Step Up</div>

    <ul class="tagline-list">
      <li>Step Up</li>
      <li class="tagline-divider">---------</li>
      <li>Personal Fitness Sessions</li>
      <li class="tagline-divider">---------</li>
      <li>Stay Bold Feel Free</li>
    </ul>

    <h2 class="holder-name">Kim Farrow</h2>
    <p class="holder-role">PT's with a passionate coach</p>

    <p class="contact-row contact-row--phone">
      <svg width="22" height="32" viewBox="0 0 22 32" aria-hidden="true">
        <rect x="2" y="1.5" width="18" height="29" rx="3" fill="none" stroke="#ffffff" stroke-width="2.5"/>
        <line x1="2" y1="6" x2="20" y2="6" stroke="#ffffff" stroke-width="2"/>
        <line x1="2" y1="25" x2="20" y2="25" stroke="#ffffff" stroke-width="2"/>
      </svg>
      <span>0431 592 604</span>
    </p>
    <p class="contact-row contact-row--email">
      <svg width="26" height="20" viewBox="0 0 26 20" aria-hidden="true">
        <path d="M1 7 L13 1 L25 7 V19 H1 Z" fill="#ffffff"/>
        <path d="M1 7 L13 14 L25 7" fill="none" stroke="#434343" stroke-width="2"/>
      </svg>
      <span>kimjoanne@wavenet.example</span>
    </p>

    <div class="activity-figures" role="img" aria-label="Grey silhouettes of people running, stretching, doing sit-ups, boxing, flexing and martial arts"></div>
  </section>

  <section class="card card--orange" aria-label="Business card, white, orange and grey version">
    <svg class="card__backdrop" viewBox="0 0 726 422" preserveAspectRatio="none" aria-hidden="true">
      <path d="M0 270 C200 240 440 172 726 196 V422 H0 Z" fill="#77747f"/>
      <path d="M300 214 C460 180 600 176 726 184" fill="none" stroke="#77747f" stroke-width="3"/>
      <path d="M0 258 C120 272 220 258 330 228" fill="none" stroke="#ef7f1f" stroke-width="6"/>
    </svg>

    <div class="brand-name">Step Up</div>

    <h2 class="holder-name">Kim Farrow</h2>
    <p class="holder-role">PT's with a passionate coach</p>

    <p class="contact-row contact-row--phone">
      <svg width="22" height="32" viewBox="0 0 22 32" aria-hidden="true">
        <rect x="2" y="1.5" width="18" height="29" rx="3" fill="none" stroke="#ef7f1f" stroke-width="2.5"/>
        <line x1="2" y1="6" x2="20" y2="6" stroke="#ef7f1f" stroke-width="2"/>
        <line x1="2" y1="25" x2="20" y2="25" stroke="#ef7f1f" stroke-width="2"/>
      </svg>
      <span>0431 592 604</span>
    </p>
    <p class="contact-row contact-row--email">
      <svg width="26" height="20" viewBox="0 0 26 20" aria-hidden="true">
        <path d="M1 7 L13 1 L25 7 V19 H1 Z" fill="#ef7f1f"/>
        <path d="M1 7 L13 14 L25 7" fill="none" stroke="#ffffff" stroke-width="2"/>
      </svg>
      <span>kimjoanne@wavenet.example</span>
    </p>

    <ul class="tagline-list">
      <li>Step Up</li>
      <li>Personal Fitness Sessions</li>
      <li>Stay Bold Feel Free</li>
    </ul>

    <div class="activity-figures" role="img" aria-label="White silhouettes of people stretching, doing sit-ups, stepping, running, boxing, flexing and martial arts"></div>
  </section>

</main>
</body>
</html>
```